Warehouse fit out company needed website design!

Colour scheme to match attached business logo (faded lemon yellow, charcoal and white.

My business is doing warehouse fit outs using heavy duty storage systems such as pallet racking, mezzanine floors, cantilever racking and shelving.

Website to be modern style and easy for the customer to navigate through.

Please visit this competitors website for example of the type of design I would like www.brindlevault.com.au

My business will be providing the exact same service and products so this will give you a great understanding of what I am chasing from my website

Target Market(s)

Small to large businesses with warehouses to store their product.

Coding

Coded - Design and coding required

Number of Pages Required

5+ page

Colors
fbed22
ffffff
1b1b1b

Requirements
Must have
• Bold banner incorporating my attached logo on each page with drop boxes for products, services, contact us
• Home page to have "about us" write up section and images
Nice to have
• Modern style layout and easy to navigate through for the client

```html
<!DOCTYPE html>
<html lang="en">
<head>
<meta charset="utf-8">
<title>Stackd Storage — Warehouse Fit Outs</title>
<link href="https://fonts.googleapis.com/css2?family=Audiowide&family=Roboto:ital,wght@0,400;0,500;0,700;1,400&display=swap" rel="stylesheet">
<style>
:root{
  --lemon:#fbed22;
  --charcoal:#1b1b1b;
  --charcoal-soft:#2a2a2a;
  --white:#ffffff;
  --text:#444444;
  --ghost:#f1f1f1;
  --display:"Audiowide", sans-serif;
  --body:"Roboto", sans-serif;
}
*{margin:0;padding:0;box-sizing:border-box}
html,body{width:1200px;height:2894px;overflow:hidden}
body{position:relative;background:var(--white);font-family:var(--body);color:var(--text)}
.abs{position:absolute}

/* header */
.site-header{position:absolute;left:0;top:0;width:1200px;height:80px;background:var(--lemon)}
.brand{position:absolute;left:146px;top:16px;font-family:var(--body);font-weight:700;font-size:40px;letter-spacing:3px;color:var(--charcoal);line-height:48px}
.main-nav{position:absolute;right:146px;top:30px;display:flex;gap:24px}
.main-nav a{font-size:16px;font-weight:500;color:var(--charcoal);text-decoration:none}

/* hero */
.hero{position:absolute;left:0;top:80px;width:1200px;height:499px;
  background:linear-gradient(180deg,#6d6f73 0%,#8a5a35 30%,#3d4e7a 55%,#b5b3ad 80%,#d4d2cc 100%)}
.hero-title{position:absolute;left:404px;top:132px;width:393px;height:87px;background:var(--charcoal);
  font-family:var(--display);font-size:72px;color:var(--lemon);text-align:center;line-height:87px;letter-spacing:2px}
.hero-sub{position:absolute;left:0;top:240px;width:1200px;text-align:center;color:var(--white);font-size:20px;line-height:31px;text-shadow:0 1px 3px rgba(0,0,0,.6)}
.btn{display:flex;align-items:center;justify-content:center;gap:8px;border-radius:30px;font-weight:500;text-decoration:none}
.btn-lemon{background:var(--lemon);color:var(--charcoal)}
.hero .btn{position:absolute;left:502px;top:321px;width:196px;height:45px;font-size:18px}
.dots{position:absolute;left:0;top:430px;width:1200px;display:flex;justify-content:center;gap:6px}
.dots span{width:12px;height:12px;border-radius:50%;border:2px solid var(--white)}
.dots span.on{background:var(--white)}

/* welcome */
.ghost{position:absolute;font-family:var(--display);color:var(--ghost);line-height:1;white-space:nowrap}
.section-title{position:absolute;left:0;width:1200px;text-align:center;font-family:var(--display);font-size:40px;color:var(--charcoal);line-height:1}
.section-title em{font-style:normal;color:var(--lemon)}
.intro{position:absolute;left:210px;top:720px;width:780px;text-align:center;font-size:14px;line-height:32px;color:#555}
.contact-lead{position:absolute;left:0;top:840px;width:1200px;text-align:center;font-size:28px;color:var(--charcoal)}
.contact-phone{position:absolute;left:0;top:880px;width:1200px;text-align:center;font-size:34px;font-weight:500;color:var(--lemon);letter-spacing:1px}
.quote-btn{position:absolute;left:502px;top:943px;width:196px;height:45px;font-size:18px}

/* gallery */
.gallery-tile{position:absolute;width:297px;height:235px}

/* systems */
.system{position:absolute;top:1733px;width:300px;height:365px;text-align:center}
.system.light{background:var(--lemon);color:var(--charcoal)}
.system.dark{background:var(--charcoal);color:var(--white)}
.system svg{position:absolute;left:112px;top:31px}
.system h3{position:absolute;left:0;top:130px;width:100%;font-size:22px;font-weight:500}
.system p{position:absolute;left:28px;top:170px;width:244px;font-size:13.5px;line-height:25px}
.system.light p{color:#333}
.system.dark p{color:#ccc}
.system .btn{position:absolute;top:289px;height:41px;font-size:13.5px;font-weight:700}
.system.light .btn{background:var(--charcoal);color:var(--lemon);left:84px;width:133px}
.system.dark .btn{border:2px solid var(--lemon);color:var(--lemon);left:83px;width:135px}

/* testimonials */
.review{position:absolute;top:2263px;height:180px;background:var(--white);border:1px solid #e3e3e3;box-shadow:0 2px 6px rgba(0,0,0,.08);text-align:center}
.review::after{content:"";position:absolute;left:50%;bottom:-9px;width:16px;height:16px;background:var(--white);border-right:1px solid #e3e3e3;border-bottom:1px solid #e3e3e3;transform:translateX(-50%) rotate(45deg)}
.review .mark{position:absolute;left:0;top:10px;width:100%;font-family:Georgia,serif;font-size:64px;font-weight:700;color:var(--lemon);line-height:1}
.review p{position:absolute;left:30px;top:60px;right:30px;font-size:12.5px;font-style:italic;line-height:22.5px;color:#555}
.author{position:absolute;top:2464px;display:flex;align-items:center;gap:8px}
.author .avatar{width:44px;height:44px;border-radius:50%;background:linear-gradient(135deg,#c9b8a6,#6e6259)}
.author b{display:block;font-size:16px;font-weight:500;color:var(--charcoal)}
.author small{display:block;font-size:11px;color:#333}

/* footer */
.site-footer{position:absolute;left:0;top:2592px;width:1200px;height:302px;background:linear-gradient(180deg,#2b2b2b,#121212)}
.foot-brand{position:absolute;left:146px;top:66px;font-weight:700;font-size:38px;letter-spacing:3px;color:var(--lemon);line-height:44px}
.socials{position:absolute;left:146px;top:126px;display:flex;gap:4px}
.socials span{width:30px;height:30px;border-radius:50%;border:2px solid var(--white)}
.foot-col{position:absolute;top:68px;color:var(--white)}
.foot-col h4{font-size:18px;font-weight:500;margin-bottom:12px}
.foot-col li{list-style:none;font-size:14.5px;line-height:29.5px;display:flex;align-items:center;gap:8px}
.foot-bar{position:absolute;left:0;top:251px;width:1200px;height:51px;background:#111;color:#ddd;font-size:11.5px;text-align:center;line-height:46px}
</style>
</head>
<body>

<header class="site-header">
  <div class="brand">STACKD</div>
  <nav class="main-nav">
    <a href="#">HOME</a><a href="#">PRODUCTS</a><a href="#">BOOK A QUOTE</a><a href="#">SERVICES</a><a href="#">ABOUT US</a><a href="#">CONTACT</a>
  </nav>
</header>

<section class="hero" role="img" aria-label="Photo of a large warehouse aisle lined with orange and blue pallet racking">
  <div class="hero-title">STACKD</div>
  <p class="hero-sub">At vero eos et accusamus et iusto odio dignissimos ducimus<br>qui blanditiis praesentium voluptatum</p>
  <a class="btn btn-lemon" href="#">GET STARTED
    <svg width="16" height="16" viewBox="0 0 16 16"><circle cx="8" cy="8" r="8" fill="#1b1b1b"/><path d="M6 4.5l4 3.5-4 3.5z" fill="#fbed22"/></svg></a>
  <div class="dots"><span></span><span></span><span class="on"></span><span></span><span></span></div>
</section>
<svg class="abs" style="left:540px;top:555px" width="120" height="25" viewBox="0 0 120 25">
  <path d="M0 25 C30 25 40 0 60 0 C80 0 90 25 120 25z" fill="#fff"/>
  <path d="M52 11l8 7 8-7" fill="none" stroke="#999" stroke-width="1.5"/>
</svg>

<div class="ghost" style="left:812px;top:880px;font-size:86px">ABOUT</div>
<h2 class="section-title" style="top:655px">WELCOME TO <em>STACKD</em></h2>
<p class="intro">At vero eos et accusamus et iusto odio dignissimos ducimus qui blanditiis praesentium voluptatum deleniti atque corrupti quos dolores et quas molestias excepturi sint occaecati cupiditate non provident, similique sunt in culpa qui officia deserunt mollitia animi, id est laborum et dolorum fugat harum quidem rerum facilis est et expedita distinctio.</p>
<p class="contact-lead">CONTACT OUR TEAM TODAY</p>
<p class="contact-phone">1 888 888 8888</p>
<a class="btn btn-lemon quote-btn" href="#">GET A QUOTE
  <svg width="16" height="16" viewBox="0 0 16 16"><circle cx="8" cy="8" r="8" fill="#1b1b1b"/><path d="M6 4.5l4 3.5-4 3.5z" fill="#fbed22"/></svg></a>

<div class="gallery-tile" style="left:146px;top:1040px;background:linear-gradient(180deg,#3a3530,#8a7a55 50%,#7c7a76)" role="img" aria-label="Photo of a narrow aisle with tall black and yellow racking"></div>
<div class="gallery-tile" style="left:452px;top:1040px;background:linear-gradient(180deg,#6f7b8c,#2f4fa0 45%,#5d6066)" role="img" aria-label="Photo of blue and orange carton flow racking along a long aisle"></div>
<div class="gallery-tile" style="left:757px;top:1040px;background:linear-gradient(180deg,#d6d6d6,#a94148 45%,#c9c9c9)" role="img" aria-label="Photo of red pallet racking in a bright warehouse"></div>
<div class="gallery-tile" style="left:146px;top:1284px;background:linear-gradient(135deg,#2a52b0,#c8b070 50%,#2a52b0)" role="img" aria-label="Photo of dense blue and orange racking viewed from above"></div>
<div class="gallery-tile" style="left:452px;top:1284px;background:linear-gradient(180deg,#3a3b3d,#5a5b5d 50%,#2f3032)" role="img" aria-label="Darkened photo of a warehouse aisle with a zoom icon">
  <svg class="abs" style="left:136px;top:105px" width="26" height="26" viewBox="0 0 26 26"><circle cx="10.5" cy="10.5" r="8" fill="none" stroke="#fff" stroke-width="3"/><path d="M16.5 16.5l7 7" stroke="#fff" stroke-width="3.5" stroke-linecap="round"/></svg>
</div>
<div class="gallery-tile" style="left:757px;top:1284px;background:linear-gradient(90deg,#b59a70,#e4e4e2 50%,#b59a70)" role="img" aria-label="Photo of shelving stacked with cardboard boxes"></div>

<div class="ghost" style="left:0;top:1612px;font-size:72px">SYSTEM</div>
<h2 class="section-title" style="top:1598px">OUR HEAVY DUTY</h2>
<h2 class="section-title" style="top:1649px;color:var(--lemon)">STORAGE SYSTEMS</h2>

<article class="system light" style="left:0">
  <svg width="76" height="76" viewBox="0 0 76 76" fill="none" stroke="#1b1b1b" stroke-width="3"><rect x="6" y="10" width="30" height="22"/><rect x="38" y="10" width="30" height="22"/><rect x="6" y="34" width="30" height="22"/><rect x="38" y="34" width="30" height="22"/><path d="M2 58h72M2 66h72M10 58v8M37 58v8M64 58v8"/></svg>
  <h3>PALLET RACKING</h3>
  <p>At vero eos et accusamus et iusto odio dignissimos ducimus qui blanditiis praesentium voluptatum deleniti corrupti quos dolores et quas molestias</p>
  <a class="btn" href="#">READ MORE <svg width="12" height="12" viewBox="0 0 16 16"><circle cx="8" cy="8" r="8" fill="#fbed22"/><path d="M6 4.5l4 3.5-4 3.5z" fill="#1b1b1b"/></svg></a>
</article>
<article class="system dark" style="left:300px">
  <svg width="76" height="76" viewBox="0 0 76 76" fill="none" stroke="#fbed22" stroke-width="3"><rect x="4" y="4" width="28" height="28"/><rect x="36" y="14" width="36" height="22"/><rect x="16" y="38" width="56" height="34"/><path d="M16 55h22M38 38v34M50 20h14"/></svg>
  <h3>MEZZANINE FLOORS</h3>
  <p>At vero eos et accusamus et iusto odio dignissimos ducimus qui blanditiis praesentium voluptatum deleniti corrupti quos dolores et quas molestias</p>
  <a class="btn" href="#">READ MORE <svg width="12" height="12" viewBox="0 0 16 16"><circle cx="8" cy="8" r="8" fill="#fbed22"/><path d="M6 4.5l4 3.5-4 3.5z" fill="#1b1b1b"/></svg></a>
</article>
<article class="system light" style="left:600px">
  <svg width="76" height="76" viewBox="0 0 76 76" fill="none" stroke="#1b1b1b" stroke-width="3"><path d="M4 2v74M72 2v74M4 26h68M4 50h68M4 74h68"/><rect x="18" y="10" width="20" height="14"/><rect x="40" y="10" width="20" height="14"/><rect x="12" y="34" width="22" height="14"/><rect x="36" y="34" width="22" height="14"/><rect x="16" y="58" width="40" height="14"/></svg>
  <h3>CANTILEVER RACKING</h3>
  <p>At vero eos et accusamus et iusto odio dignissimos ducimus qui blanditiis praesentium voluptatum deleniti corrupti quos dolores et quas molestias</p>
  <a class="btn" href="#">READ MORE <svg width="12" height="12" viewBox="0 0 16 16"><circle cx="8" cy="8" r="8" fill="#fbed22"/><path d="M6 4.5l4 3.5-4 3.5z" fill="#1b1b1b"/></svg></a>
</article>
<article class="system dark" style="left:900px">
  <svg width="76" height="76" viewBox="0 0 76 76" fill="none" stroke="#fbed22" stroke-width="3"><path d="M4 72V24L38 4l34 20v48z"/><path d="M14 72V32h48v40M14 40h48M30 14h16"/><rect x="38" y="52" width="12" height="12"/><rect x="50" y="52" width="10" height="12"/><path d="M18 70h16v-12h-10z"/></svg>
  <h3>SHELVING</h3>
  <p>At vero eos et accusamus et iusto odio dignissimos ducimus qui blanditiis praesentium voluptatum deleniti corrupti quos dolores et quas molestias</p>
  <a class="btn" href="#">READ MORE <svg width="12" height="12" viewBox="0 0 16 16"><circle cx="8" cy="8" r="8" fill="#fbed22"/><path d="M6 4.5l4 3.5-4 3.5z" fill="#1b1b1b"/></svg></a>
</article>

<div class="ghost" style="left:838px;top:2158px;font-size:72px">REVIEW</div>
<h2 class="section-title" style="top:2173px">WHAT <em>CLIENTS SAY</em></h2>

<div class="review" style="left:134px;width:302px"><div class="mark">&ldquo;</div><p>In ullamcorper est eget tempor cursus neque mi consectetuer mi a ultricies massa est sed nisl Class aptent taciti sociosqu ad litora torquent per conubia nostra</p></div>
<div class="review" style="left:449px;width:305px"><div class="mark">&ldquo;</div><p>In ullamcorper est eget tempor cursus neque mi consectetuer mi a ultricies massa est sed nisl Class aptent taciti sociosqu ad litora torquent per conubia nostra</p></div>
<div class="review" style="left:770px;width:295px"><div class="mark">&ldquo;</div><p>In ullamcorper est eget tempor cursus neque mi consectetuer mi a ultricies massa est sed nisl Class aptent taciti sociosqu ad litora torquent per conubia nostra</p></div>

<div class="author" style="left:210px"><div class="avatar" role="img" aria-label="Client portrait"></div><div><b>By Author Name</b><small>City, Location</small></div></div>
<div class="author" style="left:523px"><div class="avatar" role="img" aria-label="Client portrait"></div><div><b>By Author Name</b><small>City, Location</small></div></div>
<div class="author" style="left:846px"><div class="avatar" role="img" aria-label="Client portrait"></div><div><b>By Author Name</b><small>City, Location</small></div></div>

<footer class="site-footer">
  <div class="foot-brand">STACKD</div>
  <div class="socials"><span></span><span></span><span></span><span></span></div>
  <div class="foot-col" style="left:398px">
    <h4>CONTACT US</h4>
    <ul>
      <li><svg width="10" height="14" viewBox="0 0 10 14"><path d="M5 0a5 5 0 0 1 5 5c0 4-5 9-5 9S0 9 0 5a5 5 0 0 1 5-5z" fill="#fbed22"/><circle cx="5" cy="5" r="2" fill="#222"/></svg>110 At vero eos et aciodio dignissimos</li>
      <li><svg width="13" height="13" viewBox="0 0 13 13"><path d="M2 0l3 3-1.5 2a8 8 0 0 0 4.5 4.5L10 8l3 3-2 2C5 13 0 8 0 2z" fill="#fbed22"/></svg>Phone : 1 888 888 8888</li>
      <li><svg width="14" height="11" viewBox="0 0 14 11"><rect width="14" height="11" fill="#fbed22"/><path d="M0 0l7 6 7-6" fill="none" stroke="#222" stroke-width="1.5"/></svg>Email : info@stackd.com</li>
    </ul>
  </div>
  <div class="foot-col" style="left:727px">
    <h4>QUICK LINKS</h4>
    <ul><li>About Us</li><li>Services</li><li>Gallery</li><li>Process</li></ul>
  </div>
  <div class="foot-col" style="left:912px">
    <h4>OPENING HOUR</h4>
    <ul><li>Monday - Friday</li><li>7.30am - 5.00pm</li></ul>
  </div>
  <div class="foot-bar">&copy; 2019 Stackd. All right reserved &nbsp;Term of Use &nbsp;| &nbsp;Privacy policy</div>
</footer>
<svg class="abs" style="left:540px;top:2592px" width="120" height="25" viewBox="0 0 120 25">
  <path d="M0 0 C30 0 40 25 60 25 C80 25 90 0 120 0z" fill="#fff"/>
  <path d="M52 15l8-7 8 7" fill="none" stroke="#999" stroke-width="1.5"/>
</svg>

</body>
</html>
```